Real Estate Web Design

I need someone who can design a few elements for a real estate website. I DO NOT need the whole website designed (though if you are good i might use you for that also)

The designs Needs to be done with CSS and HTML ONLY, with placeholders for images and property data (will be dynamically inserted). I need about 4-5 designs for the following: SINGLE property display, property listings displays (boxes, cards, list views etc), and property search forms. I also need the CSS to be THEME PROOF, meaning having unique class names that don't clash with any theme (this will eventually be used with Wordpress). The designs must also be FULLY RESPONSIVE.

If i pick your design, you also agree to any tweaks or adjustments that might be needed to make it fit/work with what i need. (like naming the classes etc)

I don't mind if you use or find a really cool existing design out there, so long as you adapt it to CSS and HTML ONLY. (and it doesn't violate any copyrights of course)

Thanks! Look forward to working with you!!

PS - i have added some screenshots from the VELTRA wordpress theme. These are elements i need. but i need them UNIQUE and i need them designed ONLY with HTML and css

```html
<!DOCTYPE html>
<html lang="en">
<head>
<meta charset="utf-8">
<title>Property Card</title>
<link rel="stylesheet" href="https://fonts.googleapis.com/css2?family=Karla:wght@400;500;600&family=Open+Sans:wght@600;700&display=swap">
<style>
  :root {
    --page-bg: #ffffff;
    --badge-green: #0a8a0a;
    --text-white: #ffffff;
    --meta-text: #555555;
    --icon-grey: #666666;
    --divider: #c9c9c9;
    --meta-divider: #bdbdbd;
    --bookmark-ring: #ffffff;
    --bookmark-icon: #a89a86;
    --sky-top: #6f9fe0;
    --sky-low: #a9c6ec;
    --house-slate: #5b7080;
    --garden-green: #566b3a;
  }
  * { box-sizing: border-box; margin: 0; padding: 0; }
  html, body {
    width: 1200px;
    height: 579px;
    overflow: hidden;
    background: var(--page-bg);
  }
  .listing-canvas {
    position: relative;
    width: 1200px;
    height: 579px;
  }
  .property-card {
    position: absolute;
    left: 63px;
    top: 27px;
    width: 527px;
  }
  .property-card__media {
    position: relative;
    width: 527px;
    height: 322px;
    overflow: hidden;
  }
  .property-card__photo {
    position: absolute;
    inset: 0;
    background:
      linear-gradient(180deg, rgba(0,0,0,0) 78%, rgba(0,0,0,0.45) 100%),
      linear-gradient(180deg, var(--sky-top) 0%, var(--sky-low) 22%, var(--house-slate) 40%, var(--house-slate) 72%, var(--garden-green) 100%);
  }
  .property-card__badge {
    position: absolute;
    left: 9px;
    top: 10px;
    height: 39px;
    padding: 0 21px;
    border-radius: 20px;
    background: var(--badge-green);
    color: var(--text-white);
    font: 700 16px/39px "Open Sans", sans-serif;
  }
  .property-card__save {
    position: absolute;
    left: 461px;
    top: 9px;
    width: 56px;
    height: 56px;
    border-radius: 50%;
    background: var(--bookmark-ring);
    display: flex;
    align-items: center;
    justify-content: center;
  }
  .property-card__title {
    position: absolute;
    left: 9px;
    bottom: 6px;
    color: var(--text-white);
    font: 700 33px/1.1 "Open Sans", sans-serif;
    letter-spacing: 0.3px;
  }
  .property-card__meta {
    display: flex;
    align-items: center;
    height: 48px;
    border-bottom: 2px solid var(--divider);
    font: 500 14px/1 "Karla", sans-serif;
    text-transform: uppercase;
    color: var(--meta-text);
    letter-spacing: 0.3px;
  }
  .property-card__meta-item { padding: 0 19px; border-left: 1px solid var(--meta-divider); line-height: 24px; }
  .property-card__meta-item:first-child { padding-left: 0; border-left: none; }
  .property-card__features {
    display: flex;
    align-items: center;
    height: 60px;
    padding-left: 8px;
    font: 400 17px/1 "Karla", sans-serif;
    color: var(--icon-grey);
  }
  .feature { display: flex; align-items: center; gap: 5px; margin-right: 27px; }
  .feature svg { stroke: var(--icon-grey); fill: none; stroke-width: 1.6; }
</style>
</head>
<body>
<main class="listing-canvas">
  <article class="property-card">
    <div class="property-card__media">
      <div class="property-card__photo" role="img" aria-label="Photo of a two-storey slate blue weatherboard house with white trim, a front porch and a garden under a blue sky"></div>
      <span class="property-card__badge">Open House</span>
      <span class="property-card__save" aria-label="Save listing">
        <svg width="16" height="22" viewBox="0 0 16 22"><path d="M2 1.5h12v19l-6-5-6 5z" fill="none" stroke="var(--bookmark-icon)" stroke-width="1.6" stroke-linejoin="round"/></svg>
      </span>
      <h2 class="property-card__title">Painthouse In New York</h2>
    </div>
    <div class="property-card__meta">
      <span class="property-card__meta-item">NSW</span>
      <span class="property-card__meta-item">Minimum 7 sleeps</span>
      <span class="property-card__meta-item">$POA</span>
    </div>
    <ul class="property-card__features" style="list-style:none">
      <li class="feature" aria-label="Guests">
        <svg width="20" height="20" viewBox="0 0 20 20"><circle cx="10" cy="6" r="4"/><path d="M2 19c0-4.5 3.6-7 8-7s8 2.5 8 7"/></svg>7
      </li>
      <li class="feature" aria-label="Car spaces">
        <svg width="32" height="16" viewBox="0 0 32 16"><path d="M2 11V8l4-5h14l6 4 4 1v3z"/><circle cx="8" cy="12" r="2.5" fill="#fff"/><circle cx="24" cy="12" r="2.5" fill="#fff"/></svg>4
      </li>
      <li class="feature" aria-label="Bedrooms">
        <svg width="22" height="18" viewBox="0 0 22 18"><rect x="2" y="2" width="18" height="14" fill="var(--icon-grey)" stroke="none"/><rect x="4" y="4" width="14" height="5" fill="#fff" stroke="none"/></svg>5
      </li>
      <li class="feature" aria-label="Bathrooms">
        <svg width="16" height="22" viewBox="0 0 16 22"><path d="M3 21V4c0-2 2-3 4-2l6 4"/><path d="M10 5l4 3" stroke-width="2"/></svg>2
      </li>
      <li class="feature" aria-label="Pool">
        <svg width="20" height="18" viewBox="0 0 20 18"><circle cx="12" cy="4" r="2" fill="var(--icon-grey)" stroke="none"/><path d="M5 11l5-4 3 4"/><path d="M2 15c2-2 4 0 6-1s4 1 6 0 4-1 4-1"/></svg>No
      </li>
    </ul>
  </article>
</main>
</body>
</html>
```